Business Card Design

We are a flooring/granite/cabinet company
want a sleek and modern design card. Will send our logo. maybe our logo in 3d on card.
black card

Industry/Entity Type

Business

Contact Information for Business Card

Daniel Restrepo
company name Stonecrest Tile Depot
4728 loop 60w 78419
210-647-3928
stonecresttiledepot@mailbarn.net

```html
<!DOCTYPE html>
<html lang="en">
<head>
<meta charset="utf-8">
<title>Stonecrest Tile Depot — Business Card</title>
<link href="https://fonts.googleapis.com/css2?family=Arimo:wght@400;700&display=swap" rel="stylesheet">
<style>
  :root {
    --backdrop: #a9a9a9;
    --card-white: #ededeb;
    --card-black: #1b1b1b;
    --accent-green: #2f9a3a;
    --ink: #1e1e1e;
  }
  html, body {
    margin: 0;
    padding: 0;
    width: 1200px;
    height: 900px;
    overflow: hidden;
    background: var(--backdrop);
    font-family: "Arimo", Arial, sans-serif;
  }
  .canvas {
    position: relative;
    width: 1200px;
    height: 900px;
    display: flex;
    align-items: center;
    justify-content: center;
    gap: 60px;
  }
  .card {
    position: relative;
    width: 520px;
    height: 297px;
    background: var(--card-white);
    overflow: hidden;
    box-shadow: 0 6px 18px rgba(0,0,0,0.18);
  }
  .card-shapes {
    position: absolute;
    inset: 0;
  }
  .card-front .contact {
    position: absolute;
    left: 36px;
    top: 58px;
    color: var(--ink);
    font-size: 15px;
    line-height: 1.3;
  }
  .contact .person-name {
    font-weight: 700;
    font-size: 18px;
  }
  .contact .person-title {
    text-transform: uppercase;
    margin-bottom: 6px;
  }
  .card-front .brand {
    position: absolute;
    left: 330px;
    top: 112px;
    width: 170px;
    text-align: center;
    color: var(--accent-green);
    font-weight: 700;
    font-size: 17px;
    line-height: 1.25;
    text-transform: uppercase;
  }
  .card-back .brand {
    position: absolute;
    right: 30px;
    top: 146px;
    color: var(--ink);
    font-weight: 700;
    font-size: 19px;
    line-height: 22px;
    letter-spacing: 0.4px;
    text-transform: uppercase;
    display: flex;
    align-items: center;
    gap: 10px;
    white-space: nowrap;
  }
  .brand-square {
    flex: 0 0 14px;
    width: 14px;
    height: 14px;
    background: var(--accent-green);
  }
  .card-back .address {
    position: absolute;
    right: 120px;
    top: 198px;
    color: var(--ink);
    font-size: 15px;
    line-height: 1.3;
  }
</style>
</head>
<body>
<main class="canvas">

  <section class="card card-front" aria-label="Card front">
    <svg class="card-shapes" width="520" height="297" viewBox="0 0 520 297">
      <polygon points="250,0 520,0 520,297 340,297" fill="var(--card-black)"/>
      <line x1="40" y1="205" x2="470" y2="205" stroke="var(--accent-green)" stroke-width="1.5"/>
    </svg>
    <div class="contact">
      <div class="person-name">Daniel Restrepo</div>
      <div class="person-title">Founder &amp; CEO</div>
      <div class="person-email">stonecresttiledepot@mailbarn.net</div>
      <div class="person-phone">210-647-3928</div>
    </div>
    <div class="brand">Stonecrest<br>Tile Depot</div>
  </section>

  <section class="card card-back" aria-label="Card back">
    <svg class="card-shapes" width="520" height="297" viewBox="0 0 520 297">
      <polygon points="0,0 520,0 520,60 0,180" fill="var(--card-black)"/>
      <line x1="150" y1="186" x2="500" y2="186" stroke="var(--accent-green)" stroke-width="1.5"/>
    </svg>
    <div class="brand">
      <span class="brand-square"></span>
      <span class="brand-name">Stonecrest Tile Depot</span>
    </div>
    <div class="address">
      <div>Stonecrest Tile Depot</div>
      <div>4728 loop 60w 78419</div>
    </div>
  </section>

</main>
</body>
</html>
```